the cobalt heron

I need a direct mail post card made for potential clients to pick up the phone and call us to order

Industry/Entity Type

Call

Font styles to use
Serif

Requirements
Must have
• Photos of the coin we are selling
• an attention grabbing headline
• a strong call to action, (MUST call now!)
• The price of the coin must be included
• A classic high dollar luxury feel to the post card mailer

```html
<!DOCTYPE html>
<html lang="en">
<head>
<meta charset="utf-8">
<title>The Cobalt Heron – Postcard</title>
<link rel="stylesheet" href="https://fonts.googleapis.com/css2?family=Black+Ops+One&family=Montserrat:wght@400;500&family=Oswald:wght@500;600&display=swap">
<style>
  :root {
    --page: #e6e6e6;
    --ink: #050505;
    --panel: #111111;
    --silver: #d9d9d9;
    --silver-dark: #8a8a8a;
    --white: #ffffff;
    --line: rgba(255,255,255,0.85);
  }
  * { margin: 0; padding: 0; box-sizing: border-box; }
  html, body {
    width: 1200px; height: 994px; overflow: hidden;
    background: var(--page);
  }
  .postcard {
    position: absolute; left: 30px; top: 58px;
    width: 1140px; height: 877px; overflow: hidden;
    background:
      radial-gradient(ellipse 520px 260px at 50% 42%, rgba(255,255,255,0.16), transparent 70%),
      radial-gradient(ellipse 700px 420px at 50% 10%, rgba(80,80,80,0.45), transparent 75%),
      linear-gradient(180deg, #1a1a1a 0%, #0b0b0b 55%, var(--ink) 100%);
  }
  .flare-band {
    position: absolute; left: 0; top: 300px; width: 100%; height: 40px;
    background: radial-gradient(ellipse 50% 50% at 50% 50%, rgba(255,255,255,0.22), transparent 70%);
  }
  .coin {
    position: absolute; border-radius: 50%;
  }
  .coin--portrait {
    left: 230px; top: 98px; width: 444px; height: 444px;
    background: radial-gradient(circle at 45% 40%, #3a3a3a 0%, #1a1a1a 55%, #9a9a9a 88%, #e8e8e8 94%, #444 100%);
  }
  .coin--reverse {
    left: 644px; top: 210px; width: 278px; height: 278px;
    background: radial-gradient(circle at 50% 45%, #cfcfcf 0%, #a8a8a8 60%, #e6e6e6 88%, #7a7a7a 100%);
  }
  .coin-glint {
    position: absolute; border-radius: 50%;
    background: radial-gradient(circle, rgba(255,255,255,0.95), rgba(255,255,255,0) 70%);
  }
  .glint-a { left: 480px; top: 80px; width: 90px; height: 90px; }
  .glint-b { left: 860px; top: 200px; width: 80px; height: 80px; }
  .rule {
    position: absolute; left: 170px; width: 800px; height: 2px;
    background: linear-gradient(90deg, transparent, var(--line) 25%, var(--white) 50%, var(--line) 75%, transparent);
  }
  .rule--top { top: 481px; }
  .rule--bottom { top: 630px; }
  .headline {
    position: absolute; left: 0; top: 502px; width: 100%;
    text-align: center;
    font-family: "Black Ops One", sans-serif; font-size: 62px; letter-spacing: 1px;
    color: var(--silver);
    background: linear-gradient(180deg, #ffffff 0%, #d0d0d0 45%, #8f8f8f 60%, #e6e6e6 100%);
    -webkit-background-clip: text; background-clip: text; -webkit-text-fill-color: transparent;
    text-transform: uppercase; line-height: 1;
  }
  .tagline {
    position: absolute; left: 0; top: 582px; width: 100%;
    text-align: center;
    font-family: "Montserrat", sans-serif; font-weight: 500; font-size: 30px;
    letter-spacing: 12px; color: var(--white); line-height: 1;
  }
  .price-row { position: absolute; top: 678px; left: 0; width: 100%; height: 54px; }
  .price-tag {
    position: absolute; top: 0; width: 350px; height: 54px;
    display: flex; align-items: center; justify-content: center;
    font-family: "Oswald", sans-serif; font-weight: 500; font-size: 40px;
    color: var(--white); text-transform: uppercase;
  }
  .price-tag svg { position: absolute; inset: 0; }
  .price-tag span { position: relative; }
  .price-tag--one { left: 202px; }
  .price-tag--two { left: 586px; }
  .price-link {
    position: absolute; left: 552px; top: 26px; width: 34px; height: 2px;
    background: var(--silver-dark);
  }
  .offer-copy {
    position: absolute; left: 28px; top: 776px; width: 634px;
    font-family: "Montserrat", sans-serif; font-size: 19.5px; line-height: 26px;
    color: var(--white); text-align: justify;
  }
  .call-button {
    position: absolute; left: 738px; top: 776px; width: 364px; height: 75px;
    border-radius: 12px;
    background: linear-gradient(180deg, #6a6a6a 0%, #2a2a2a 48%, #0d0d0d 52%, #222 100%);
    border: 2px solid #9a9a9a;
    display: flex; align-items: center; justify-content: center; gap: 12px;
    font-family: "Oswald", sans-serif; font-weight: 600; font-size: 50px;
    color: var(--white); text-transform: uppercase; line-height: 1;
  }
</style>
</head>
<body>
  <main class="postcard">
    <div class="flare-band"></div>

    <div class="coin coin--portrait" role="img" aria-label="Photo of the silver five pound coin, portrait side"></div>
    <div class="coin coin--reverse" role="img" aria-label="Photo of the two ounce fine silver coin, reverse side"></div>
    <div class="coin-glint glint-a"></div>
    <div class="coin-glint glint-b"></div>

    <div class="rule rule--top"></div>
    <h1 class="headline">The Cobalt Heron</h1>
    <p class="tagline">WE'RE MEANT FOR YOU</p>
    <div class="rule rule--bottom"></div>

    <div class="price-row">
      <div class="price-tag price-tag--one">
        <svg viewBox="0 0 350 54" width="350" height="54" aria-hidden="true">
          <polygon points="14,1 336,1 349,27 336,53 14,53 1,27" fill="#050505" stroke="#bdbdbd" stroke-width="1.5"/>
        </svg>
        <span>Price goes here</span>
      </div>
      <div class="price-link"></div>
      <div class="price-tag price-tag--two">
        <svg viewBox="0 0 350 54" width="350" height="54" aria-hidden="true">
          <polygon points="14,1 336,1 349,27 336,53 14,53 1,27" fill="#050505" stroke="#bdbdbd" stroke-width="1.5"/>
        </svg>
        <span>Price goes here</span>
      </div>
    </div>

    <p class="offer-copy">Lorem Ipsum is simply dummy text of the printing and typesetting industry. Lorem Ipsum is simply dummy text of the printing and typesetting industry.</p>

    <div class="call-button">
      <svg width="26" height="42" viewBox="0 0 26 42" aria-hidden="true">
        <path d="M20 3 C10 3 5 12 5 21 C5 30 10 39 20 39" fill="none" stroke="#fff" stroke-width="4" stroke-linecap="round"/>
        <rect x="15" y="1" width="9" height="9" rx="2" fill="#fff"/>
        <rect x="15" y="32" width="9" height="9" rx="2" fill="#fff"/>
      </svg>
      <span>Call now!</span>
    </div>
  </main>
</body>
</html>
```